Lionel Arbusto and Dwight Halvorsen Advertisement

We would like an ad that conveys understated elegance. We are a company that purchases estate jewelry watches and diamonds. We care to a wealthy, upscale clientele.

Target Market(s)

Wealthy upscale.

Industry/Entity Type

It Company

Requirements
Must have
• Elegant Design. Crisp Clean. Attached a doc of how the ad should be arranged.

```html
<!DOCTYPE html>
<html lang="en">
<head>
<meta charset="utf-8">
<title>Lionel Arbusto &amp; Dwight Halvorsen — Ready to Sell</title>
<link rel="stylesheet" href="https://fonts.googleapis.com/css2?family=Cinzel:wght@400&family=Jost:wght@500&family=Lato:wght@400&family=Raleway:wght@300;400&display=swap">
<style>
  :root {
    --backdrop: #cfcfcf;
    --ink: #1a1a1a;
    --ink-soft: #3a3a3a;
    --rule: #6b6b6b;
    --marble-light: #f4f4f3;
    --marble-mid: #dcdcda;
    --marble-vein: #c9c2b4;
    --gem-light: #f7f7f7;
    --gem-mid: #c8c8c8;
    --gem-dark: #6e6e6e;
  }
  * { margin: 0; padding: 0; box-sizing: border-box; }
  html, body {
    width: 1200px;
    height: 1200px;
    overflow: hidden;
    background: var(--backdrop);
  }
  .ad {
    position: absolute;
    left: 167px;
    top: 40px;
    width: 892px;
    height: 1154px;
    transform: scale(0.97);
    transform-origin: top left;
    overflow: hidden;
    color: var(--ink);
  }
  .ad__marble {
    position: absolute;
    inset: 0;
    background:
      linear-gradient(115deg, transparent 38%, rgba(201,194,180,0.45) 48%, transparent 58%),
      linear-gradient(120deg, transparent 62%, rgba(180,172,158,0.35) 70%, transparent 78%),
      linear-gradient(160deg, var(--marble-light) 0%, var(--marble-mid) 45%, var(--marble-light) 70%, var(--marble-mid) 100%);
  }
  .ad__headline {
    position: absolute;
    top: 88px;
    left: 0;
    right: 0;
    text-align: center;
    font-family: "Raleway", sans-serif;
    font-weight: 300;
    font-size: 68px;
    letter-spacing: 1px;
    line-height: 1;
  }
  .ad__gem {
    position: absolute;
    left: 312px;
    top: 262px;
    width: 266px;
    height: 290px;
    border-radius: 14px;
    background: radial-gradient(circle at 50% 45%, var(--gem-light) 0%, var(--gem-mid) 60%, var(--gem-dark) 100%);
    transform: rotate(4deg);
  }
  .brand {
    position: absolute;
    top: 664px;
    left: 0;
    right: 0;
    text-align: center;
  }
  .brand__name {
    font-family: "Cinzel", serif;
    font-weight: 400;
    font-size: 23px;
    color: var(--ink-soft);
    line-height: 1;
  }
  .brand__tagline {
    margin: 8px auto 0;
    width: 370px;
    display: flex;
    align-items: center;
    gap: 8px;
    font-family: "Cinzel", serif;
    font-size: 10px;
    letter-spacing: 1px;
    color: var(--ink-soft);
  }
  .brand__tagline::before,
  .brand__tagline::after {
    content: "";
    flex: 1;
    height: 1px;
    background: var(--rule);
  }
  .promise {
    position: absolute;
    top: 948px;
    left: 0;
    right: 0;
    text-align: center;
  }
  .promise__title {
    font-family: "Raleway", sans-serif;
    font-weight: 400;
    font-size: 32px;
    letter-spacing: 6px;
    line-height: 1;
  }
  .promise__note {
    margin-top: 4px;
    font-family: "Lato", sans-serif;
    font-size: 15px;
    line-height: 1;
  }
  .contact {
    position: absolute;
    top: 1070px;
    left: 0;
    right: 0;
    text-align: center;
    font-family: "Jost", sans-serif;
    font-weight: 500;
    font-size: 11px;
    line-height: 16px;
  }
  .contact__venue {
    font-size: 14px;
    letter-spacing: 2px;
    line-height: 18px;
  }
</style>
</head>
<body>
  <main class="ad">
    <div class="ad__marble" role="img" aria-label="White marble texture with soft grey and gold veining"></div>

    <h1 class="ad__headline">READY TO SELL?</h1>

    <div class="ad__gem" role="img" aria-label="Photograph of a large square emerald-cut diamond"></div>

    <div class="brand">
      <p class="brand__name">Lionel Arbusto &amp; Dwight Halvorsen</p>
      <p class="brand__tagline">YOUR BEST OPTION</p>
    </div>

    <div class="promise">
      <p class="promise__title">UTMOST DISCRETION</p>
      <p class="promise__note">BY APPOINTMENT ONLY</p>
    </div>

    <address class="contact" style="font-style: normal;">
      <p class="contact__venue">CASA SERENA</p>
      <p>118-B Harbor Row, Coral Bay, FL 33999</p>
      <p>support@arbustohalvorsen.com | 555.014.2270</p>
    </address>
  </main>
</body>
</html>
```